Marina Web Page

I'm looking for a visually engaging web page/layout that I can use as the basis for a website for my Marina. I need to include page content that can be stored and updated in an include file to allow someone to easily manage content without editing html or needing to understand html.

The business is a small marina and fishing center located on the Pamlico sound in eastern North Carolina right off the Intracoastal Waterway. We offer wet slips with power, water, and wifi and also have powered RV slips for camping available. The Marina sells fuel, beer, tackle/bait, and ice. The Marina also has an island style bar (The Gullwing Bar) and live music most weekends. The bar has a mascot named Dusty, short for captain, who is a black labradoodle know for diving to the bottom of the marina basin to retrieve oysters and rocks. Dusty could be incorporated as a minor design element but isn't a requirement.The marina caters to coastal sportsmen interested in sound fishing as well as offshore sport fishing. The Marina also offers fishing charters form a 32' Brinewood fishing boat w/ tuna tower.

The primary purpose of the initial version of the website is to communicate information about up coming events, music, bar specials etc... It will also be used to feature our services, fishing report and weather info, where we are located from both land and water, and a photo gallery.

Target Market(s)

Coastal sports enthusiast and the coastal boating community

Industry/Entity Type

Business

Requirements
Must have
• I would like animated menus incorporated into the page temple. It must also allow for the updating/storing of page content in a separate file to that an employee of the marina can update specials and events without having to understand or edit html.
Nice to have
• A photo gallery option that will present photos from a folder on the web server. Changing photos should be as easy as adding or deleting photos from the folder.

```html
<!DOCTYPE html>
<html lang="en">
<head>
<meta charset="utf-8">
<title>Harbor Reach Marina</title>
<link rel="stylesheet" href="https://fonts.googleapis.com/css2?family=PT+Sans:wght@400;700&display=swap">
<style>
  :root {
    --page-bg: #e6e6e6;
    --panel-bg: #ffffff;
    --bar-dark: #58585a;
    --text-main: #444446;
    --text-dark: #2b2b2b;
    --teal: #17a39a;
    --orange: #ea5a2a;
    --blue: #1f6fb3;
    --brand: #2a6db5;
    --light-grey: #eeeeee;
  }
  * { margin: 0; padding: 0; box-sizing: border-box; }
  html, body { width: 944px; height: 1200px; overflow: hidden; }
  body {
    background: var(--page-bg);
    font-family: "PT Sans", sans-serif;
    color: var(--text-main);
    position: relative;
  }
  .abs { position: absolute; }

  /* Brand */
  .brand {
    left: 0; width: 944px; top: 70px;
    display: flex; justify-content: center; align-items: center; gap: 10px;
  }
  .brand-mark { width: 26px; height: 26px; border-radius: 50%; background: var(--brand); }
  .brand-name { font-size: 28px; font-weight: 700; color: var(--brand); }

  /* Navigation */
  .main-nav {
    left: 89px; top: 176px; width: 784px; height: 73px;
    background: var(--panel-bg); border: 2px solid #b3b3b3;
  }
  .nav-item { position: absolute; top: 24px; font-size: 19px; color: var(--text-main); }
  .nav-item.active {
    top: -1px; height: 71px; width: 109px; padding-top: 26px;
    background: var(--bar-dark); color: #fff; text-align: center;
  }
  .dropdown { left: 461px; top: 250px; width: 109px; z-index: 2; }
  .dropdown-item { height: 34px; font-size: 14px; text-align: center; line-height: 33px; }
  .dropdown-item.current { background: var(--bar-dark); color: #fff; }
  .dropdown-item.other { background: var(--light-grey); color: var(--text-main); margin-top: 1px; }

  /* Hero */
  .hero {
    left: 99px; top: 267px; width: 764px; height: 360px;
    background: linear-gradient(160deg, #2b3c4c 0%, #40566a 45%, #6f8494 70%, #dfe6ea 85%, #55697a 100%);
    box-shadow: 0 2px 4px rgba(0,0,0,.35);
  }
  .hero-dots { right: 18px; bottom: 8px; display: flex; gap: 10px; }
  .hero-dot { width: 20px; height: 20px; border-radius: 50%; background: #505052; border: 1px solid #8a8a8a; }

  /* Panels */
  .panel { background: var(--panel-bg); }
  .panel-head {
    height: 40px; background: var(--bar-dark); color: #fff;
    font-size: 17px; padding: 10px 0 0 13px;
  }
  .news { left: 99px; top: 643px; width: 406px; height: 388px; }
  .weather { left: 520px; top: 643px; width: 343px; height: 182px; }
  .event { left: 520px; top: 846px; width: 343px; height: 185px; }

  .teal-title { color: var(--teal); font-size: 17px; position: absolute; }
  .rule { position: absolute; height: 1px; background: var(--teal); }
  .copy { position: absolute; font-size: 10.5px; line-height: 13.7px; color: var(--text-main); }
  .copy.small { font-size: 9.6px; line-height: 12.2px; }
  .read-more { position: absolute; font-size: 8px; color: var(--teal); text-decoration: underline; }

  .news-photo {
    left: 19px; top: 260px; width: 153px; height: 102px;
    background: linear-gradient(135deg, #5e8a3a, #2a2a2a 50%, #7aa04a);
    border: 1px solid var(--teal);
  }
  .event-photo {
    left: 17px; top: 62px; width: 143px; height: 105px; border-radius: 10px;
    background: linear-gradient(180deg, #8fa6c2 0%, #b9c6d4 40%, #6e7f8c 70%, #4d5248 100%);
    border: 2px solid var(--teal);
  }

  /* Weather */
  .day-label { position: absolute; color: var(--teal); font-size: 17px; }
  .temp { position: absolute; font-size: 36px; font-weight: 700; }
  .temp.warm { color: var(--orange); }
  .temp.cool { color: var(--blue); }
  .stats { position: absolute; border-collapse: separate; border-spacing: 5px 2px; }
  .stats td {
    background: var(--teal); color: #fff; font-size: 9px; font-weight: 700;
    height: 14px; padding: 0 3px; line-height: 14px;
  }
  .stats td.value { text-align: center; width: 51px; font-weight: 400; }
  .stats td.key { width: 66px; }
  .divider { position: absolute; left: 168px; top: 60px; width: 1px; height: 106px; background: var(--teal); }

  /* Footer */
  .site-footer {
    left: 102px; top: 1046px; width: 761px; height: 49px;
    background: var(--bar-dark); color: var(--text-dark);
    font-size: 13px; text-align: center; line-height: 49px;
  }
</style>
</head>
<body>

<div class="abs brand">
  <span class="brand-mark"></span>
  <span class="brand-name">Harbor Reach Marina</span>
</div>

<nav class="abs main-nav">
  <span class="nav-item" style="left:37px">Home</span>
  <span class="nav-item" style="left:143px">News</span>
  <span class="nav-item" style="left:257px">Services</span>
  <span class="nav-item active" style="left:370px">Tools</span>
  <span class="nav-item" style="left:523px">Photo Galery</span>
  <span class="nav-item" style="left:675px">Contact</span>
</nav>
<div class="abs dropdown">
  <div class="dropdown-item current">Weather Info</div>
  <div class="dropdown-item other">Fishing report</div>
</div>

<section class="abs hero" role="img" aria-label="Sport fishing boat with tuna tower speeding across dark choppy water, white wake behind">
  <div class="abs hero-dots">
    <span class="hero-dot"></span><span class="hero-dot"></span><span class="hero-dot"></span><span class="hero-dot"></span>
  </div>
</section>

<section class="abs panel news">
  <div class="panel-head">LATEST NEWS</div>
  <h3 class="teal-title" style="left:19px;top:55px;font-weight:400">NEWS TITLE</h3>
  <div class="rule" style="left:13px;top:83px;width:369px"></div>
  <p class="copy" style="left:21px;top:100px;width:360px">Lorem ipsum dolor sit amet, consectetur adipiscing elit. Vestibulum suscipit semper metus, nec malesuada nibh congue vitae. Nulla facilisi. Aenean nec mi vitae ligula pellentesque posuere eu at justo. In non laoreet est. Vestibulum cursus est lorem, a ullamcorper risus consectetur eget. Proin euismod, nisl sed egestas molestie, nulla urna sodales sem, nec bibendum velit ligula sed dolor. Nunc ullamcorper placerat molestie. Fusce ut ultrices</p>
  <span class="read-more" style="left:341px;top:187px">Read more</span>
  <h3 class="teal-title" style="left:19px;top:206px;font-weight:400">NEWS TITLE</h3>
  <div class="rule" style="left:13px;top:234px;width:369px"></div>
  <div class="abs news-photo" role="img" aria-label="Black curly-coated dog lying on green grass"></div>
  <p class="copy small" style="left:178px;top:265px;width:208px">Lorem ipsum dolor sit amet, consectetur adipiscing elit. Vestibulum suscipit semper metus, nec malesuada nibh congue vitae. Nulla facilisi. Aenean nec mi vitae ligula pellentesque posuere eu at justo. In non laoreet est. Vestibulum cursus est lorem, a ullamcorper risus consectetur eget.</p>
  <span class="read-more" style="left:342px;top:340px">Read more</span>
</section>

<section class="abs panel weather">
  <div class="panel-head">WEATHER INFO</div>
  <span class="day-label" style="left:26px;top:61px">TODAY</span>
  <svg class="abs" style="left:104px;top:54px" width="36" height="36" viewBox="0 0 36 36" aria-hidden="true">
    <g stroke="#f6b800" stroke-width="2.5" stroke-linecap="round">
      <line x1="18" y1="2" x2="18" y2="7"/><line x1="18" y1="29" x2="18" y2="34"/>
      <line x1="2" y1="18" x2="7" y2="18"/><line x1="29" y1="18" x2="34" y2="18"/>
      <line x1="6.7" y1="6.7" x2="10.2" y2="10.2"/><line x1="25.8" y1="25.8" x2="29.3" y2="29.3"/>
      <line x1="6.7" y1="29.3" x2="10.2" y2="25.8"/><line x1="25.8" y1="10.2" x2="29.3" y2="6.7"/>
    </g>
    <circle cx="18" cy="18" r="8.5" fill="#f9c400"/>
  </svg>
  <span class="temp warm" style="left:55px;top:91px">25°C</span>
  <table class="stats" style="left:26px;top:137px">
    <tr><td class="key">Humidity</td><td class="value">71%</td></tr>
    <tr><td class="key">Wind Speed</td><td class="value">10 km/h</td></tr>
  </table>
  <div class="divider"></div>
  <span class="day-label" style="left:178px;top:60px">TOMORROW</span>
  <svg class="abs" style="left:280px;top:52px" width="54" height="38" viewBox="0 0 54 38" aria-hidden="true">
    <path d="M12 28 a8 8 0 0 1 2-15 a11 11 0 0 1 21-3 a9 9 0 0 1 12 9 a6 6 0 0 1-2 9 z" fill="#dfe3e8" stroke="#9aa3ad" stroke-width="1"/>
    <g stroke="#4a7fc0" stroke-width="2" stroke-linecap="round">
      <line x1="20" y1="31" x2="18" y2="35"/><line x1="28" y1="31" x2="26" y2="35"/><line x1="36" y1="31" x2="34" y2="35"/>
    </g>
  </svg>
  <span class="temp cool" style="left:218px;top:88px">10°C</span>
  <table class="stats" style="left:191px;top:136px">
    <tr><td class="key">Humidity</td><td class="value">10%</td></tr>
    <tr><td class="key">Wind Speed</td><td class="value">1 km/h</td></tr>
  </table>
</section>

<section class="abs panel event">
  <div class="panel-head">NEXT EVENT</div>
  <div class="abs event-photo" role="img" aria-label="Blue waterfront bar building with a lookout tower under a pale sky"></div>
  <h3 class="teal-title" style="left:199px;top:60px;font-size:13px;font-weight:700">BAND NAME</h3>
  <div class="rule" style="left:176px;top:80px;width:143px"></div>
  <p class="copy small" style="left:174px;top:87px;width:160px">Lorem ipsum dolor sit amet, consectetur adipisicing elit, sed do eiusmod tempor incididunt ut labore et dolore magna aliqua. Ut enim ad minim veniam, quis</p>
  <span class="read-more" style="left:287px;top:149px">Read more</span>
</section>

<footer class="abs site-footer">Copyright Marina Company &nbsp;|&nbsp; Terms and Conditions &nbsp;|&nbsp; Contact</footer>

</body>
</html>
```